New more attractive design for an old tired look that is high tech but inviting

Need a more modern eye catching design. We are and I/T and MSP and we need a new look. Need a call to action on each page. Needs to be in WordPress. Existing site is quorbelna.com. Needs to work on phones and tablets. The default home page should present us as an MSP/MSSP and direct the viewer to our services we offer.
Updates

Current deadline assigned at project inception has passed before project started

Need extra days to review

Target Market(s)

Our target market is other businesses. We do not target residential customers.

Industry/Entity Type

Business to Business oriented

Coding

Coded - Design and coding required

Number of Pages Required

5+ page

Font styles to use
Sans Serif

Requirements
Must have
• Must have a current relevant design with a call to action on each page.
Nice to have
• Dark background high tech look with people to make it attractive

```html
<!DOCTYPE html>
<html lang="en">
<head>
<meta charset="utf-8">
<title>Quorbelna – Data Center Services</title>
<link href="https://fonts.googleapis.com/css2?family=Roboto:ital,wght@0,300;0,400;0,500;0,700;0,900;1,300&display=swap" rel="stylesheet">
<style>
:root{
  --navy:#12122b;
  --navy-2:#1b1b3d;
  --red:#e0323c;
  --red-soft:#e8545c;
  --mist:#d5d8e5;
  --ink:#1a1a33;
  --body:#3a3a4a;
  --white:#ffffff;
  --line:rgba(255,255,255,.25);
}
*{margin:0;padding:0;box-sizing:border-box}
html,body{width:685px;height:1200px;overflow:hidden;background:var(--white)}
body{font-family:'Roboto',sans-serif;position:relative;color:var(--ink)}
.abs{position:absolute}
.on-dark{color:var(--white)}

/* hero */
.hero{left:0;top:0;width:685px;height:275px;background:radial-gradient(ellipse at 80% 95%,#2a2a52 0%,var(--navy) 60%)}
.brand{left:122px;top:11px;font-size:15px;font-weight:700;letter-spacing:.2px}
.nav{left:262px;top:19px;display:flex;gap:21px;font-size:5.8px;font-weight:500;letter-spacing:.1px}
.nav-active{left:258px;top:44px;width:24px;height:1.5px;background:var(--white)}
.phone-btn{left:497px;top:13px;width:68px;height:19px;border:.7px solid var(--white);border-radius:3px;display:flex;align-items:center;justify-content:center;gap:4px;font-size:5.3px;font-weight:700}
.head-rule{left:120px;top:45.5px;width:445px;height:.6px;background:var(--line)}
.hero-title{left:120px;top:92px;font-size:47px;font-weight:900;letter-spacing:1px;line-height:1;display:flex;align-items:center;gap:8px}
.hero-title-red{left:121px;top:139px;font-size:47px;font-weight:900;letter-spacing:1.5px;line-height:1;color:var(--red-soft)}
.hero-copy{left:356px;top:150px;width:170px;font-size:6.8px;line-height:9.6px;letter-spacing:.15px}
.hero-copy b{font-weight:700}
.btn{display:flex;align-items:center;justify-content:space-between;border:.7px solid currentColor;border-radius:4px;font-size:5.3px;font-weight:500;padding-left:11px;letter-spacing:.1px}
.btn .arrow{width:15px;height:100%;border-radius:0 4px 4px 0;background:rgba(255,255,255,.15);display:flex;align-items:center;justify-content:center}
.explore{left:125px;top:199px;width:80px;height:23px}

/* about */
.about{left:0;top:275px;width:685px;height:260px;background:var(--mist)}
.about-mark{left:128px;top:318px;font-size:36px;font-weight:700;color:#b9bccb;line-height:1}
.about-title{left:120px;top:402px;font-size:17.5px;font-weight:500;line-height:23px;color:var(--ink)}
.about-title .red{color:var(--red)}
.about-copy{left:348px;top:326px;width:218px;font-size:6px;line-height:9.9px;color:var(--body);font-weight:300}
.about-copy p+p{margin-top:9.9px}

/* stats */
.stats{left:120px;top:480px;width:445px;height:108px;border-radius:20px;background:linear-gradient(135deg,#1f1f46 0%,var(--navy) 70%);display:flex;justify-content:space-around;padding:0 10px}
.stat{width:100px;text-align:center;padding-top:31px}
.stat-num{font-size:25px;font-weight:700;color:var(--red-soft);line-height:1}
.stat-label{font-size:5.8px;font-weight:500;margin-top:7px;letter-spacing:.2px}

/* services */
.services-title{left:112px;top:681px;font-size:17.5px;font-weight:500;line-height:23px}
.services-title .red{color:var(--red)}
.all-btn{left:112px;top:736px;width:80px;height:23px;color:var(--ink)}
.all-btn .arrow{background:#e6e7ee}
.card{width:142px}
.card svg{display:block}
.card h3{font-size:8.2px;font-weight:500;margin-top:19px;color:var(--ink)}
.card p{font-size:5.9px;line-height:9.9px;color:var(--body);margin-top:9px;font-weight:300}

/* cta */
.cta{left:0;top:960px;width:685px;height:240px;background:radial-gradient(ellipse at 50% 80%,#1f1f44 0%,var(--navy) 65%)}
.cta-title{left:0;top:1000px;width:685px;text-align:center;font-size:31px;font-weight:700;display:flex;justify-content:center;align-items:center;gap:6px}
.cta-title .red{color:var(--red-soft)}
.cta-sub{left:0;top:1048px;width:685px;text-align:center;font-size:13.5px;font-weight:300;font-style:italic}
.cta-sub b{font-style:normal;font-weight:500}
.contact-btn{left:299px;top:1087px;width:87px;height:23px}
.foot-rule{left:120px;top:1163px;width:445px;height:.6px;background:var(--line)}
.foot-copy{left:120px;top:1178px;font-size:5.2px}
.foot-links{right:120px;top:1178px;font-size:5.2px}
</style>
</head>
<body>

<section class="abs hero" role="img" aria-label="Dark navy backdrop with faint hexagon network and wave pattern"></section>
<div class="abs brand on-dark">Quorbelna</div>
<nav class="abs nav on-dark"><span>HOME</span><span>SERVICES</span><span>ABOUT US</span><span>CONTACT</span></nav>
<div class="abs nav-active"></div>
<div class="abs head-rule"></div>
<div class="abs phone-btn on-dark">
  <svg width="6" height="6" viewBox="0 0 24 24"><path fill="#fff" d="M6.6 10.8a15 15 0 006.6 6.6l2.2-2.2c.3-.3.7-.4 1-.2 1.1.4 2.3.6 3.6.6.6 0 1 .4 1 1V20c0 .6-.4 1-1 1A17 17 0 013 4c0-.6.4-1 1-1h3.5c.6 0 1 .4 1 1 0 1.3.2 2.5.6 3.6.1.3 0 .7-.2 1z"/></svg>
  555-014-2273
</div>

<h1 class="abs hero-title on-dark">DATA
  <svg width="30" height="34" viewBox="0 0 30 34" fill="none" stroke="#fff" stroke-width="2.2"><ellipse cx="15" cy="5" rx="13" ry="4"/><path d="M2 5v24c0 2.2 5.8 4 13 4s13-1.8 13-4V5"/><path d="M2 13c0 2.2 5.8 4 13 4s13-1.8 13-4M2 21c0 2.2 5.8 4 13 4s13-1.8 13-4"/><g fill="#fff" stroke="none"><circle cx="22" cy="12" r="1"/><circle cx="25" cy="11" r="1"/><circle cx="22" cy="20" r="1"/><circle cx="25" cy="19" r="1"/><circle cx="22" cy="28" r="1"/><circle cx="25" cy="27" r="1"/></g></svg>
  CENTER</h1>
<div class="abs hero-title-red">SERVICES</div>
<p class="abs hero-copy on-dark">We offer colocation, virtualization, storage as a service and disaster recovery out of our own <b>enterprise-grade</b> data center.</p>
<a class="abs btn explore on-dark">EXPLORE MORE <span class="arrow"><svg width="6" height="6" viewBox="0 0 10 10" stroke="#fff" stroke-width="1.4" fill="none"><path d="M2 8L8 2M3 2h5v5"/></svg></span></a>

<section class="abs about"></section>
<div class="abs about-mark">Quorbelna</div>
<h2 class="abs about-title">About<br><span class="red">Quorbelna</span> Group</h2>
<div class="abs about-copy">
  <p>Like most great businesses Quorbelna began in a gargage during the summer of 1995 in Brookhaven, SC. It was a part time venture by Marcus Delvane and his business partner Owen Trask. They had discovered an opportunity in technology sales and service after a combined 30 years at Halvern Power in information technology. By 2000, the two set out on their own and were working on the venture full-time.</p>
  <p>Today, the company has grown significantly and continues to do so. Quorbelna provides services including multi-dwelling unit managed networks, data center services, low voltage wiring and local office IT support. Industries served include: retail, manufacturing, MDUs, hospitality, software development, medical, construction and more.</p>
</div>

<div class="abs stats on-dark">
  <div class="stat"><div class="stat-num">22</div><div class="stat-label">YEARS IN BUSINESS</div></div>
  <div class="stat"><div class="stat-num">2</div><div class="stat-label">OWNERS</div></div>
  <div class="stat"><div class="stat-num">1</div><div class="stat-label">LOCATION</div></div>
  <div class="stat"><div class="stat-num">11</div><div class="stat-label">EMPLOYEES</div></div>
</div>

<h2 class="abs services-title">Our<br><span class="red">Services</span></h2>
<a class="abs btn all-btn">ALL SERVICES <span class="arrow"><svg width="6" height="6" viewBox="0 0 10 10" stroke="#1a1a33" stroke-width="1.4" fill="none"><path d="M2 8L8 2M3 2h5v5"/></svg></span></a>

<svg width="0" height="0" style="position:absolute">
  <symbol id="shield-hand" viewBox="0 0 46 48">
    <g fill="none" stroke="#1a1a33" stroke-width="1.6" stroke-linejoin="round" stroke-linecap="round">
      <path d="M23 2l11 5v9c0 8-5 13-11 16C17 29 12 24 12 16V7z"/>
      <circle cx="23" cy="16" r="6"/>
      <path d="M20 16l2.5 2.5L27 13"/>
      <path d="M9 12C4 14 2 17 3 19l3 1M37 12c5 2 7 5 6 7l-3 1"/>
      <path d="M4 38h5v9H4zM9 40l7-3h8c2 0 2 3 0 3h-6M24 40l9-5c2-1 4 1 2 3l-9 7H9"/>
    </g>
  </symbol>
</svg>

<article class="abs card" style="left:272px;top:640px"><svg width="44" height="46"><use href="#shield-hand"/></svg><h3>Managed Networks for MDUs</h3><p>High speed internet is now the number one amenity for multi-dwelling units. It needs to be fast, always online and have excellent coverage around the clock.</p></article>
<article class="abs card" style="left:432px;top:640px"><svg width="44" height="46"><use href="#shield-hand"/></svg><h3>Data Center Services</h3><p>Quorbelna offers a full suite of data center services through our VaultFrame® brand. We work with your organization to develop a solution to meet the unique needs of your business.</p></article>
<article class="abs card" style="left:112px;top:789px"><svg width="44" height="46"><use href="#shield-hand"/></svg><h3>Cyber Security</h3><p>60% of small businesses hit by a cyberattack go out of business within 6 months. But enterprise-level security has always been out of reach — until now. Starting at just $15/month.</p></article>
<article class="abs card" style="left:272px;top:789px"><svg width="44" height="46"><use href="#shield-hand"/></svg><h3>Low Voltage Wiring</h3><p>To keep everyone connected with the outside world, modern buildings run on many different technologies. All of these systems must communicate over the right cabling installed the right way.</p></article>
<article class="abs card" style="left:432px;top:789px"><svg width="44" height="46"><use href="#shield-hand"/></svg><h3>Office IT Support</h3><p>Quorbelna offers a full suite of data center services through our VaultFrame® brand. We work with your organization to develop a solution to meet the unique needs of your business.</p></article>

<section class="abs cta" role="img" aria-label="Dark navy backdrop with faint wave pattern"></section>
<h2 class="abs cta-title on-dark">Do you need an IT
  <svg width="20" height="22" viewBox="0 0 20 22" fill="none" stroke="#fff" stroke-width="1.2" stroke-linecap="round"><circle cx="12" cy="7" r="4"/><path d="M10.5 11v2h3v-2M12 1V0M6 3l-1-1M18 3l1-1M2 16h3v5H2zM5 17l4-1.5h4c1 0 1 1.5 0 1.5h-3M13 17l4-2c1 0 2 1 1 1.5L13 20H5"/></svg>
  <span class="red">Solution?</span></h2>
<p class="abs cta-sub on-dark">Start now with <b>Quorbelna</b></p>
<a class="abs btn contact-btn on-dark">CONTACT US NOW <span class="arrow"><svg width="6" height="6" viewBox="0 0 10 10" stroke="#fff" stroke-width="1.4" fill="none"><path d="M2 8L8 2M3 2h5v5"/></svg></span></a>
<div class="abs foot-rule"></div>
<div class="abs foot-copy on-dark">2025 © Quorbelna of SC, Inc.</div>
<div class="abs foot-links on-dark">Home | Services | About | Contact | Privacy Policy | Terms &amp; Conditions</div>

</body>
</html>
```